Criação de Folder para Advocacia e Direito
" É um escritório de Advocacia onde trabalho sozinho para um atendimento personalíssimo do cliente, tal qual um atelier "

```html
<!DOCTYPE html>
<html lang="pt-BR">
<head>
<meta charset="UTF-8">
<title>Folder – Rafael Moreira Lima Advocacia</title>
<link rel="stylesheet" href="https://fonts.googleapis.com/css2?family=Montserrat:wght@300;400;600;700;800&display=swap">
<style>
  :root {
    --ink: #1d2a31;
    --ink-soft: #34434b;
    --paper: #f4f5f5;
    --mist: #c9cfd2;
    --canvas: #e6e8e9;
    --text-muted: #5d6a70;
  }
  * { box-sizing: border-box; margin: 0; padding: 0; }
  html, body { width: 1200px; height: 1200px; overflow: hidden; }
  body {
    background: var(--canvas);
    font-family: "Montserrat", sans-serif;
    color: var(--ink);
  }
  .spread {
    position: absolute;
    left: 50px; top: 220px;
    width: 1100px; height: 760px;
    display: flex;
    box-shadow: 0 10px 30px rgba(0,0,0,.18);
  }
  .page { position: relative; width: 550px; height: 760px; overflow: hidden; }

  /* Left page */
  .page--about { background: var(--ink); color: var(--paper); }
  .monogram-decor {
    position: absolute; left: 0; top: 0; width: 550px; height: 470px;
    background: linear-gradient(135deg, var(--paper) 0%, var(--mist) 45%, var(--ink-soft) 100%);
    clip-path: polygon(0 0, 100% 0, 100% 100%, 0 62%);
  }
  .about { position: absolute; left: 40px; top: 470px; width: 300px; }
  .about__kicker { font-size: 13px; font-weight: 400; letter-spacing: 1.5px; text-transform: uppercase; }
  .about__title { font-size: 15px; font-weight: 800; letter-spacing: 1px; text-transform: uppercase; margin-bottom: 10px; }
  .about p { font-size: 9.5px; line-height: 1.45; font-weight: 300; margin-bottom: 10px; }

  .brand {
    position: absolute; left: 40px; top: 660px;
    display: flex; align-items: center; gap: 12px;
  }
  .brand__mark { width: 34px; height: 34px; border: 2px solid var(--paper); border-radius: 50%; }
  .brand__name { font-size: 20px; font-weight: 400; line-height: 1.05; letter-spacing: 1px; text-transform: uppercase; }
  .brand__tag { font-size: 7px; letter-spacing: 1.5px; text-transform: uppercase; margin-top: 4px; font-weight: 400; }

  /* Right page */
  .page--services { background: var(--paper); }
  .services-decor {
    position: absolute; left: 0; top: 0; width: 260px; height: 420px;
    background: linear-gradient(160deg, var(--ink) 0%, var(--ink-soft) 100%);
    clip-path: polygon(0 0, 100% 0, 8% 100%, 0 100%);
  }
  .expertise { position: absolute; right: 40px; top: 60px; width: 240px; text-align: right; }
  .section-title { font-size: 15px; font-weight: 400; letter-spacing: 1px; text-transform: uppercase; margin-bottom: 10px; }
  .section-title strong { font-weight: 800; }
  .expertise p { font-size: 9.5px; line-height: 1.45; color: var(--text-muted); margin-bottom: 8px; }
  .expertise h4 { font-size: 9px; font-weight: 700; margin: 4px 0 6px; }

  .areas { position: absolute; left: 200px; top: 330px; width: 320px; }
  .areas .section-title { text-align: left; margin-bottom: 18px; }
  .areas__grid { display: flex; gap: 30px; }
  .area { width: 145px; }
  .area__icon { width: 22px; height: 22px; margin-bottom: 8px; display: block; }
  .area__title { font-size: 10px; font-weight: 800; text-transform: uppercase; margin-bottom: 6px; }
  .area p { font-size: 9px; line-height: 1.45; color: var(--text-muted); }

  .claim-band {
    position: absolute; left: 0; bottom: 60px; width: 550px; height: 60px;
    background: var(--ink); color: var(--paper);
    display: flex; align-items: center; justify-content: space-between;
    padding: 0 40px 0 150px;
  }
  .claim { font-size: 11px; line-height: 1.3; }
  .claim strong { font-weight: 700; }
  .claim--right { text-align: right; }
</style>
</head>
<body>
  <main class="spread">
    <section class="page page--about">
      <div class="monogram-decor" role="img" aria-label="Grande monograma da marca como elemento decorativo em faixas diagonais"></div>
      <div class="about">
        <p class="about__kicker">Sobre o</p>
        <h2 class="about__title">Rafael Moreira Lima</h2>
        <p>Lorem ipsum dolor sit amet, consectetur adipiscing elit, sed do eiusmod tempor incididunt ut labore et dolore magna aliqua. Ut enim ad minim veniam, quis nostrud exercitation.</p>
        <p>Lorem ipsum dolor sit amet, consectetur adipiscing elit, sed do eiusmod tempor incididunt ut labore et dolore magna aliqua.</p>
      </div>
      <div class="brand">
        <span class="brand__mark"></span>
        <div>
          <div class="brand__name">Rafael Moreira<br>Lima</div>
          <div class="brand__tag">Escritório Individual de Advocacia</div>
        </div>
      </div>
    </section>

    <section class="page page--services">
      <div class="services-decor" role="img" aria-label="Continuação do monograma decorativo em faixa diagonal escura"></div>
      <div class="expertise">
        <h2 class="section-title">Nossa <strong>Expertise</strong></h2>
        <p>Lorem ipsum dolor sit amet, consectetur adipiscing elit, sed do eiusmod tempor incididunt ut labore et dolore magna aliqua. Ut enim ad minim veniam.</p>
        <h4>Missão, Visão &amp; Valores</h4>
        <p>Lorem ipsum dolor sit amet, consectetur adipiscing elit, sed do eiusmod tempor incididunt ut labore et dolore magna aliqua. Ut enim ad minim veniam, quis nostrud exercitation.</p>
      </div>

      <div class="areas">
        <h2 class="section-title">Áreas de <strong>Atuação</strong></h2>
        <div class="areas__grid">
          <article class="area">
            <svg class="area__icon" viewBox="0 0 24 24" fill="none" stroke="#1d2a31" stroke-width="1.6" aria-hidden="true">
              <circle cx="7" cy="15" r="4.5"/><circle cx="17" cy="15" r="4.5"/><path d="M10 9h4M7 10.5V7h10v3.5"/>
            </svg>
            <h3 class="area__title">Direito Penal</h3>
            <p>Lorem ipsum dolor sit amet, consectetur adipiscing elit, sed do eiusmod tempor incididunt ut labore et dolore magna aliqua. Ut enim ad minim veniam.</p>
          </article>
          <article class="area">
            <svg class="area__icon" viewBox="0 0 24 24" fill="none" stroke="#1d2a31" stroke-width="1.6" aria-hidden="true">
              <rect x="3" y="7" width="18" height="13" rx="1.5"/><path d="M9 7V4.5h6V7M3 12h18"/>
            </svg>
            <h3 class="area__title">Direito Empresarial</h3>
            <p>Lorem ipsum dolor sit amet, consectetur adipiscing elit, sed do eiusmod tempor incididunt ut labore et dolore magna aliqua. Ut enim ad minim veniam.</p>
          </article>
        </div>
      </div>

      <div class="claim-band">
        <p class="claim"><strong>Confiança &amp; Seriedade em</strong><br>Direito Penal / Empresarial</p>
        <p class="claim claim--right"><strong>Advocacia Personalizada</strong> para<br>sua solução ideal.</p>
      </div>
    </section>
  </main>
</body>
</html>
```